WordPress Website for Pain Relief Clinic

I need a WordPress website designed for my laser pain relief clinic. It needs to be a professional, responsive design with 7 pages: Home, Why Choose Us, Treatable Conditions, Testimonials, FAQ, Franchising, Contact Us. Here is logo: https://files.brivoltcdn.com/media.t-w-e-n.com/sitebuilder/472/CalvexaLogoHighQuality.png

Target Market(s)

people with pain,elderly adults,injuries,soreness

Industry/Entity Type

Clinic

Number of Pages Required

5+ page

Colors
0792cd
85abd2

```html
<!DOCTYPE html>
<html lang="en">
<head>
<meta charset="utf-8">
<title>Calvexa Pain Treatment Center</title>
<link href="https://fonts.googleapis.com/css2?family=Open+Sans:ital,wght@0,400;0,600;0,700;0,800;1,400;1,600&display=swap" rel="stylesheet">
<style>
:root{
  --brand:#0792cd;
  --brand-dark:#0a5fa8;
  --brand-soft:#85abd2;
  --accent:#e8402c;
  --ink:#2b2f36;
  --muted:#8a8f97;
  --light:#f3f5f8;
  --footer:#0d1626;
  --footer-deep:#08101c;
  --white:#ffffff;
}
*{box-sizing:border-box;margin:0;padding:0}
html,body{width:1200px;height:2432px;overflow:hidden}
body{font-family:"Open Sans",Arial,sans-serif;color:var(--ink);background:var(--white);position:relative}
.site{position:relative;width:1200px;height:2432px;overflow:hidden}
.btn{display:inline-block;background:var(--brand-dark);color:var(--white);font-size:13px;font-weight:600;padding:10px 22px;border-radius:2px}
.lorem{font-size:13px;line-height:22px;color:var(--muted)}

/* header */
.header{position:absolute;top:0;left:0;width:1200px;height:140px;background:var(--white)}
.brand{position:absolute;left:178px;top:34px;display:flex;align-items:center;gap:12px}
.brand-mark{width:22px;height:22px;background:var(--brand)}
.brand-name{font-size:40px;font-weight:800;color:var(--brand-dark);letter-spacing:-1px;line-height:1}
.brand-tag{position:absolute;left:212px;top:82px;font-size:10px;letter-spacing:4px;color:var(--brand-dark);font-weight:600}
.toplinks{position:absolute;right:180px;top:12px;display:flex;gap:14px;font-size:11px;color:var(--muted)}
.phone{position:absolute;right:180px;top:34px;font-size:15px;font-weight:700;color:var(--brand-dark)}
.phone span{color:var(--muted);font-weight:400;font-size:12px}
.nav{position:absolute;right:180px;top:80px;display:flex;align-items:center;gap:22px;font-size:12px;font-weight:600;color:var(--ink)}
.nav .active{color:var(--brand)}
.nav .btn{padding:8px 14px;font-size:12px;background:var(--brand)}
.header-rule{position:absolute;left:0;bottom:0;width:100%;height:4px;background:var(--brand)}

/* hero */
.hero{position:absolute;top:140px;left:0;width:1200px;height:400px;background:linear-gradient(90deg,#f4f6f8 0%,#eef1f4 40%,#d7dde3 65%,#bfc7cf 100%)}
.hero-photo{position:absolute;right:0;top:0;width:640px;height:400px;background:linear-gradient(110deg,rgba(238,241,244,0) 0%,#c9d1d8 30%,#e1a57a 60%,#b7bfc8 100%)}
.hero-copy{position:absolute;left:210px;top:120px;width:330px}
.hero-title{font-size:34px;font-weight:800;color:var(--ink);letter-spacing:.5px}
.hero-title em{font-style:normal;color:var(--accent)}
.hero-copy .lorem{margin:12px 0 18px;font-size:12px;line-height:19px}
.dots{position:absolute;left:232px;top:350px;display:flex;gap:6px}
.dots i{width:9px;height:9px;border-radius:50%;background:#b7c0c9}
.dots i.on{background:var(--brand)}

/* conditions strip */
.strip{position:absolute;top:540px;left:0;width:1200px;height:180px;background:linear-gradient(90deg,#1c3f6e,#3c6ea8 50%,#1c3f6e)}
.strip-cards{position:absolute;left:210px;top:38px;display:flex;gap:10px}
.card{position:relative;width:146px;height:106px;background:linear-gradient(150deg,#c9b6a4,#8d98a6)}
.card span{position:absolute;left:0;bottom:0;width:100%;background:var(--brand-dark);color:var(--white);font-size:10px;font-weight:600;text-align:center;padding:4px 0}
.strip-arrow{position:absolute;top:78px}

/* why */
.why{position:absolute;top:720px;left:0;width:1200px;height:450px;background:var(--white)}
.why-photo{position:absolute;left:0;top:30px;width:580px;height:420px;background:linear-gradient(120deg,#e9e2dc,#caa58a 45%,#e4e6ea)}
.why-copy{position:absolute;left:615px;top:96px;width:400px}
.section-title{font-size:28px;font-weight:700;color:var(--ink);margin-bottom:18px}
.why-copy .lorem{margin-bottom:14px}
.lorem b{color:var(--brand-dark)}

/* quote */
.quote{position:absolute;top:1170px;left:0;width:1200px;height:100px;background:var(--brand-dark);display:flex;align-items:center;padding-left:212px}
.quote p{color:var(--white);font-style:italic;font-size:17px;font-weight:600}

/* treatable */
.treat{position:absolute;top:1270px;left:0;width:1200px;height:300px}
.treat-copy{position:absolute;left:212px;top:50px;width:400px}
.treat-photo{position:absolute;right:0;top:0;width:560px;height:300px;background:linear-gradient(135deg,#e6e9ee,#c5a28a 55%,#9aa3ad)}

/* testimonials */
.testi{position:absolute;top:1570px;left:0;width:1200px;height:330px;background:var(--light)}
.testi .section-title{text-align:center;margin:36px 0 20px}
.testi-cols{display:flex;gap:40px;justify-content:center}
.testi-cols p{width:330px;font-size:12px;line-height:19px;color:var(--muted)}
.avatar{position:absolute;left:576px;top:194px;width:48px;height:48px;border-radius:50%;background:linear-gradient(#6b7a8c,#2f3d52)}
.person{position:absolute;left:0;top:254px;width:100%;text-align:center}
.person strong{display:block;font-size:13px}
.person span{font-size:11px;color:var(--muted)}

/* newsletter */
.news{position:absolute;top:1900px;left:0;width:1200px;height:170px;background:linear-gradient(100deg,#0a4f96,#1677c2 50%,#0a4f96);display:flex;align-items:center}
.news h2{position:absolute;left:212px;font-size:22px;font-weight:600;color:var(--white);letter-spacing:.5px}
.news-form{position:absolute;left:590px;display:flex;gap:10px}
.field{width:170px;height:34px;background:var(--white);font-size:11px;color:var(--muted);padding:10px}
.news-form .btn{height:34px;padding:9px 18px;background:var(--brand-dark);border:1px solid var(--brand-soft)}

/* footer */
.footer{position:absolute;top:2070px;left:0;width:1200px;height:362px;background:var(--footer)}
.fcol{position:absolute;top:46px;color:#c4ccd7}
.fcol h3{font-size:14px;font-weight:700;color:var(--white);margin-bottom:14px}
.fcol p,.fcol li{font-size:11px;line-height:20px;list-style:none}
.about{left:234px;width:230px}
.social{display:flex;gap:6px;margin-top:12px}
.social i{width:22px;height:22px;background:#c4ccd7}
.links{left:576px}
.contact{left:840px}
.copyright{position:absolute;bottom:0;left:0;width:100%;height:44px;background:var(--footer-deep);text-align:center;font-size:10px;color:#7f8897;line-height:44px}
</style>
</head>
<body>
<div class="site">

  <header class="header">
    <div class="brand"><span class="brand-mark"></span><span class="brand-name">Calvexa</span></div>
    <div class="brand-tag">PAIN TREATMENT CENTER</div>
    <div class="toplinks"><span>Blog</span><span>Franchising</span><span>FAQ</span><span>Contact Us</span></div>
    <div class="phone"><span>Call Us Now:</span> (+61 5550 0198)</div>
    <nav class="nav">
      <span class="active">Home</span><span>Why Choose Us</span><span>Treatable Conditions</span><span>Testimonials</span>
      <span class="btn">Request a Quote</span>
    </nav>
    <div class="header-rule"></div>
  </header>

  <section class="hero">
    <div class="hero-photo" role="img" aria-label="Patient wearing orange safety glasses receiving laser treatment from a clinician"></div>
    <div class="hero-copy">
      <h1 class="hero-title">WE RELIEVE <em>PAIN</em></h1>
      <p class="lorem">Gentle laser care that eases aches and helps the body heal. Our team treats chronic pain, sports injuries and daily soreness with calm, proven methods.</p>
      <span class="btn">Get Started</span>
    </div>
    <div class="dots"><i class="on"></i><i></i><i></i></div>
  </section>

  <section class="strip">
    <svg class="strip-arrow" style="left:168px" width="20" height="26" viewBox="0 0 20 26"><path d="M15 2 4 13l11 11" fill="none" stroke="#fff" stroke-width="3"/></svg>
    <div class="strip-cards">
      <div class="card" role="img" aria-label="Back pain treatment"><span>Relieve Back Pain</span></div>
      <div class="card" role="img" aria-label="Knee pain treatment"><span>Relieve Knee Pain</span></div>
      <div class="card" role="img" aria-label="Shoulder pain treatment"><span>Relieve Shoulder Pain</span></div>
      <div class="card" role="img" aria-label="Neck pain treatment"><span>Relieve Neck Pain</span></div>
      <div class="card" role="img" aria-label="Hip pain treatment" style="width:60px"></div>
    </div>
    <svg class="strip-arrow" style="left:1014px" width="20" height="26" viewBox="0 0 20 26"><path d="M5 2l11 11L5 24" fill="none" stroke="#fff" stroke-width="3"/></svg>
  </section>

  <section class="why">
    <div class="why-photo" role="img" aria-label="Smiling patient wearing red laser safety glasses"></div>
    <div class="why-copy">
      <h2 class="section-title">Why Choose Us?</h2>
      <p class="lorem">Our clinic combines modern laser therapy with caring staff who listen first. Each plan is shaped around your body, your routine and your goals. <b>Quick visits, no drugs, no surgery.</b> Most patients feel relief within a few sessions.</p>
      <p class="lorem">We work with older adults, athletes and busy workers alike. Treatments are safe, painless and backed by years of clinical practice across many conditions. <b>Book a free consult today.</b></p>
      <span class="btn">Read More</span>
    </div>
  </section>

  <section class="quote">
    <p>"Under certain circumstances, profanity provides a relief denied even to prayer."</p>
  </section>

  <section class="treat">
    <div class="treat-copy">
      <h2 class="section-title">Treatable Conditions</h2>
      <p class="lorem">From arthritis and back pain to tendon strain and nerve pain, laser therapy reduces swelling and speeds repair. <b>Gentle care for lasting results.</b> Ask us how it can help you.</p>
      <p class="lorem" style="margin:12px 0 18px">We also treat plantar pain, tennis elbow, neck stiffness and more. <b>Full list inside.</b></p>
      <span class="btn">Read More</span>
    </div>
    <div class="treat-photo" role="img" aria-label="Clinician applying a laser device to a patient's shoulder"></div>
  </section>

  <section class="testi">
    <h2 class="section-title">What People Say About Us?</h2>
    <div class="testi-cols">
      <p>After years of knee pain I could finally walk my dog again. The staff were kind and every visit was quick and easy. I recommend this clinic to all my friends.</p>
      <p>My shoulder felt better after only three visits. The team explained each step and never rushed me. Real care, real results and a warm welcome each time.</p>
    </div>
    <div class="avatar" role="img" aria-label="Portrait of reviewer"></div>
    <div class="person"><strong>John Doe</strong><span>Manager</span></div>
  </section>

  <section class="news">
    <h2>SUBSCRIBE TO NEWSLETTER</h2>
    <div class="news-form">
      <div class="field">Name</div>
      <div class="field">Email</div>
      <span class="btn">Subscribe</span>
    </div>
  </section>

  <footer class="footer">
    <div class="fcol about">
      <h3>About Us</h3>
      <p>We are a laser pain relief clinic helping people move freely again. Safe, gentle care for every age, every day of the week.</p>
      <div class="social"><i></i><i></i><i></i><i></i></div>
    </div>
    <div class="fcol links">
      <h3>Quick Links</h3>
      <ul><li>Home</li><li>Why Choose Us</li><li>Treatable Conditions</li><li>Testimonials</li><li>Blog</li><li>Franchising</li><li>FAQ</li><li>Contact Us</li></ul>
    </div>
    <div class="fcol contact">
      <h3>Contact Info</h3>
      <p>48 Harbour Lane, Westfield</p>
      <p>Suite 12, Level 2</p>
      <p style="margin-top:10px">hello@calvexa-clinic.com</p>
      <p>(+61 5550 0198)</p>
    </div>
    <div class="copyright">Copyright © 2024 Calvexa. All Rights Reserved.</div>
  </footer>

</div>
</body>
</html>
```